Fitness Centre/Personal Trainer Business Card

We need a business card design for a company based in Singapore called 'Vigor Summit'.

We are a team of Personal Trainers and we are planning to open our new training facility.

This design will also be printed/painted on the walls in our gym.

We are a new breed of personal trainers who take fitness seriously and holistically. We do not merely train our clients to be big and muscular.

We believe in wholeness. In our opinion, fitness should include: strength, speed, flexibility, mobility, stamina & agility. These are what we train for. Of course, nutrition/diet is key.

We use fitness tools such as kettlebells, QLV, Pylometric boxes, battling ropes, clubbells, medicine balls, bulgarian bags etc - functional and non-bulky tools.

I currently have a Facebook page 'Vigor Summit SG' which shows a logo of a kettlebell. But my business focus has since changed.

Services provided:
- Kettlebell Sport Preparation
- Calisthenics Training
- Corrective Exercises
- Sports Strength & Conditioning
- 28 days Weight Loss Program
- Myofascial Rehab Therapy
- Sports/Thai Massage

Main colors for the design should be BLACK & YELLOW. We envision a design which is able to protray the holistic view we take on fitness. Also it should somewhat appeal to the ladies and not intimidate them.

Target Market(s)

People between 18-35 years old. Students and working class alike.

Industry/Entity Type

Training

Requirements
Must have
• Name: Marcus Oleander Pryce
Fitness Coach
Corrective Exercise Specialist
M: +65 9372 6058
E: marcus@sgvigorsummit-example.com

Double-sided please.
Nice to have
• "What is your vigor summit?"

```html
<!DOCTYPE html>
<html lang="en">
<head>
<meta charset="utf-8">
<title>Vigor Summit – Business Card</title>
<link rel="stylesheet" href="https://fonts.googleapis.com/css2?family=Poiret+One&family=Delius&display=swap">
<style>
  :root {
    --paper: #ffffff;
    --frame: #fff200;
    --card: #111111;
    --accent: #e6e01c;
    --title: #f4f1c6;
    --title-font: "Poiret One", sans-serif;
    --body-font: "Delius", cursive;
  }
  * { margin: 0; padding: 0; box-sizing: border-box; }
  html, body {
    width: 1200px; height: 819px; overflow: hidden;
    background: var(--paper);
  }
  .sheet { position: relative; width: 1200px; height: 819px; }

  .card {
    position: absolute;
    background: var(--frame);
    padding: 9px;
  }
  .card__face {
    position: relative; width: 100%; height: 100%;
    background: var(--card);
    border-radius: 0 18px 0 18px;
    color: var(--accent);
    font-family: var(--body-font);
    overflow: hidden;
  }
  .card--landscape { width: 491px; height: 284px; }
  .card--portrait { width: 266px; height: 446px; }
  .card--front-wide { left: 45px; top: 165px; }
  .card--back-wide { left: 45px; top: 480px; }
  .card--front-tall { left: 584px; top: 42px; }
  .card--back-tall { left: 876px; top: 42px; }

  .abs { position: absolute; white-space: nowrap; }

  .brand {
    font-family: var(--title-font);
    color: var(--title);
    font-weight: 400;
    line-height: 1;
  }
  .contact { font-size: 12px; line-height: 1.55; }
  .contact__name { font-size: 14px; letter-spacing: 0.5px; }
  .contact__email { font-size: 11px; }

  .services__title { font-size: 17px; letter-spacing: 1px; color: #f1ecd0; font-weight: 400; }
  .services__list { list-style: none; font-size: 12px; line-height: 21.5px; margin-top: 4px; }

  .tagline { color: #e9e6c9; font-size: 15px; }
</style>
</head>
<body>
<main class="sheet">

  <!-- Landscape front -->
  <section class="card card--landscape card--front-wide">
    <div class="card__face">
      <div class="abs contact" style="left:16px; top:13px;">
        <div class="contact__name">MARCUS OLEANDER PRYCE</div>
        <div>Fitness Coach</div>
        <div class="contact__email">E: marcus@sgvigorsummit-example.com</div>
      </div>
      <div class="abs brand" style="right:20px; top:166px; font-size:42px;">Vigor Summit</div>
      <div class="abs tagline" style="right:26px; top:221px;">What Is Your Vigor Summit?</div>
    </div>
  </section>

  <!-- Landscape back -->
  <section class="card card--landscape card--back-wide">
    <div class="card__face">
      <div class="abs brand" style="right:20px; top:14px; font-size:33px;">Vigor Summit</div>
      <div class="abs services" style="left:16px; top:76px;">
        <h2 class="services__title">SERVICES PROVIDED</h2>
        <ul class="services__list">
          <li>Kettlebell Sport Preparation</li>
          <li>Calisthenics Training</li>
          <li>Corrective Exercises</li>
          <li>Sports Strength &amp; Conditioning</li>
          <li>28 days Weight Loss Program</li>
          <li>Myofascial Rehab Therapy</li>
          <li>Sports/Thai Massage</li>
        </ul>
      </div>
      <div class="abs contact" style="left:250px; top:162px; line-height:1.5;">
        <div class="contact__name" style="font-size:13px;">MARCUS OLEANDER PRYCE</div>
        <div>Fitness Coach</div>
        <div>Corrective Exercise Specialist</div>
        <div>M: +65 9372 6058</div>
        <div class="contact__email" style="font-size:10px;">E: marcus@sgvigorsummit-example.com</div>
      </div>
    </div>
  </section>

  <!-- Portrait front -->
  <section class="card card--portrait card--front-tall">
    <div class="card__face">
      <div class="abs brand" style="left:0; right:14px; top:24px; text-align:center; font-size:44px; line-height:0.8;">
        <div style="padding-left:80px;">Vigor</div>
        <div style="padding-left:80px;">Summit</div>
      </div>
      <div class="abs tagline" style="left:30px; top:290px; font-size:16px; line-height:1.25;">
        What Is Your<br>Vigor Summit?
      </div>
      <div class="abs contact" style="left:30px; top:340px;">
        <div class="contact__name" style="font-size:13px;">MARCUS OLEANDER PRYCE</div>
        <div>Fitness Coach</div>
        <div class="contact__email" style="font-size:10.5px;">E: marcus@sgvigorsummit-example.com</div>
      </div>
    </div>
  </section>

  <!-- Portrait back -->
  <section class="card card--portrait card--back-tall">
    <div class="card__face">
      <div class="abs brand" style="left:15px; top:24px; font-size:29px;">Vigor Summit</div>
      <div class="abs services" style="left:15px; top:82px;">
        <h2 class="services__title" style="font-size:16px;">SERVICES PROVIDED</h2>
        <ul class="services__list" style="line-height:21.3px;">
          <li>Kettlebell Sport Preparation</li>
          <li>Calisthenics Training</li>
          <li>Corrective Exercises</li>
          <li>Sports Strength &amp; Conditioning</li>
          <li>28 days Weight Loss Program</li>
          <li>Myofascial Rehab Therapy</li>
          <li>Sports/Thai Massage</li>
        </ul>
      </div>
      <div class="abs contact" style="left:20px; top:313px; line-height:1.45;">
        <div class="contact__name" style="font-size:14px;">MARCUS OLEANDER PRYCE</div>
        <div>Fitness Coach</div>
        <div>Corrective Exercise Specialist</div>
        <div>M: +65 9372 6058</div>
        <div class="contact__email" style="font-size:10px;">E: marcus@sgvigorsummit-example.com</div>
      </div>
    </div>
  </section>

</main>
</body>
</html>
```